Book Cover for Collection of Dark Short Stories

I need a cover design for my book "Amber Harbors." It will be a 5 x 8 paperback roughly 200 pages long. There will be 11 short stories in it of a darker nature. The book is a mixture of science fiction, historical fiction, and just interesting to read stories. The stories focus on individuals or people facing difficult situations such as terrifying end of the world scenarios, mortal danger in wars, as well as crushing debt and a job layoff.
I envision the cover with dark colors (blue/black). One suggestion is to have the silhouette of a man outside sitting on a log or hill with him looking slightly down in contemplation. There are dark clouds covering most of the sky, but the stars and/or moon are trying to shine through in one small area. There's a small amount of hope in the gloom.
I see the mood of the cover as darkly reflective.

I will be happy to look at other suggestions, too.

I will also have some text on the back with a small author photo in the middle. I see the back cover as a continuation of the front cover with dark clouds and again the small amount of light from the moon and stars.
I don't want any violence or death in the cover.
I'll be happy to look at suggestions for the back cover area from the designers.
Updates

The title of the book is: AMBER HARBORS a subtitle in a smaller font somewhere below should read: A Collection of Short Stories My name should be at the bottom of the cover: Dale Marbury

Hey designers, Please find the text for the back cover here: This fascinating collection of short stories is a unique blend of science fiction, action, and historical fiction that will entertain and challenge you. In Amber Harbors’ 11 intriguing stories, we experience one isolated man’s survival as he holds out and awaits the terrifying arrival of otherworldly visitors; firsthand battlefield accounts with some strange occurrences in both WW II and the Revolutionary War; and a tiger hunt in India that goes very wrong. We also see tales of modern woe revolving around some of life’s common miseries, accompanied by brave and unexpected measures to fight against them. In addition, we witness an awkward and dangerous stay in an underground bunker with an unstable host; two astronauts stranded on a lifeless asteroid who only have one old-fashioned form of entertainment; an eerie post-plague world dominated by an unlikely species; and an eccentric astronaut orbiting the Earth who is happiest on his own, except for one furry exception. Dale Marbury’s interesting stories travel in different directions, but spring from one deep source: the darker side of the imagination. I also have an author photo that I would like either below the text or in between, whichever looks better. Feel free to crop it without my hands or whatever looks best.

Target Market(s)

Men 18-65, but crossover appeal to women is fine, too.

Font styles to use
Serif

Colors
0255a3
000000
1b1b1b
dcdcdc
fbf289

Requirements
Must have
• AMBER HARBORS in some form.
Nice to have
• Some interesting takes on AMBER HARBORS and the silhouette of a man sitting and contemplating deep things (like the end of the world).
Should not have
• No violence, sex, death, or anything provocative in the cover. I want to convey a serious, dark contemplative mood with a slight amount of hope.

```html
<!DOCTYPE html>
<html lang="en">
<head>
<meta charset="utf-8">
<title>Amber Harbors — Dale Marbury</title>
<link href="https://fonts.googleapis.com/css2?family=Bebas+Neue&family=Crimson+Text:ital@0;1&display=swap" rel="stylesheet">
<style>
  :root {
    --cream: #fbe6ad;
    --body-text: #e9e2d2;
    --sky-top: #1f2c3d;
    --sky-mid: #5f6f80;
    --horizon: #9aa6b0;
    --glow: #f0a43a;
    --ground: #0c172a;
    --ground-deep: #081222;
    --photo-slot: #ffffff;
  }
  html, body {
    margin: 0;
    padding: 0;
    width: 1200px;
    height: 919px;
    overflow: hidden;
    background: var(--ground-deep);
  }
  .cover {
    position: relative;
    width: 1200px;
    height: 919px;
    overflow: hidden;
    font-family: "Crimson Text", Georgia, serif;
  }
  .cover-scene {
    position: absolute;
    inset: 0;
    background:
      radial-gradient(ellipse 220px 90px at 1090px 385px, rgba(255,190,90,0.95), rgba(240,164,58,0.55) 45%, rgba(240,164,58,0) 100%),
      radial-gradient(ellipse 520px 140px at 980px 395px, rgba(240,164,58,0.45), rgba(240,164,58,0) 100%),
      radial-gradient(ellipse 700px 120px at 600px 360px, rgba(170,182,192,0.55), rgba(170,182,192,0) 100%),
      radial-gradient(ellipse 380px 160px at 780px 60px, rgba(150,162,175,0.5), rgba(150,162,175,0) 100%),
      linear-gradient(180deg, var(--sky-top) 0%, #34465a 18%, var(--sky-mid) 32%, var(--horizon) 41%, #3b4a5e 48%, #1a2639 60%, var(--ground) 78%, var(--ground-deep) 100%);
  }
  .title-caps {
    position: absolute;
    margin: 0;
    font-family: "Bebas Neue", Impact, sans-serif;
    font-weight: 400;
    color: var(--cream);
    text-align: center;
  }
  .back-title {
    left: 40px;
    width: 456px;
    top: 34px;
    font-size: 112px;
    line-height: 88px;
  }
  .back-blurb {
    position: absolute;
    left: 66px;
    top: 229px;
    width: 446px;
    color: var(--body-text);
    font-size: 14.8px;
    line-height: 19.2px;
    text-align: justify;
    hyphens: auto;
  }
  .back-blurb p { margin: 0 0 19px; }
  .author-photo-slot {
    position: absolute;
    left: 66px;
    top: 609px;
    width: 125px;
    height: 153px;
    background: var(--photo-slot);
  }
  .author-bio-name {
    left: 208px;
    top: 612px;
    font-size: 29px;
    line-height: 30px;
    text-align: left;
  }
  .author-bio-rule {
    position: absolute;
    left: 208px;
    top: 647px;
    width: 303px;
    height: 2px;
    background: var(--cream);
  }
  .author-bio {
    position: absolute;
    left: 208px;
    top: 658px;
    width: 303px;
    margin: 0;
    color: var(--body-text);
    font-style: italic;
    font-size: 14.4px;
    line-height: 19.4px;
    text-align: justify;
  }
  .spine-text {
    left: 582px;
    top: 279px;
    writing-mode: vertical-rl;
    font-size: 35px;
    line-height: 36px;
    letter-spacing: 0.5px;
    white-space: nowrap;
  }
  .spine-text .gap { display: inline-block; height: 24px; }
  .front-author {
    left: 640px;
    width: 552px;
    top: 36px;
    font-size: 90px;
    line-height: 80px;
  }
  .front-title {
    left: 640px;
    width: 552px;
    top: 546px;
    font-size: 170px;
    line-height: 134px;
  }
  .front-subtitle {
    left: 640px;
    width: 552px;
    top: 834px;
    font-size: 34px;
    line-height: 36px;
  }
</style>
</head>
<body>
<main class="cover">
  <div class="cover-scene" role="img" aria-label="Wraparound photograph of a cloudy evening sky over distant mountains, with a sunset glow on the right and a silhouetted man standing on a hilltop looking out"></div>

  <section class="back-cover">
    <h2 class="title-caps back-title">AMBER<br>HARBORS</h2>
    <div class="back-blurb">
      <p>This fascinating collection of short stories is a unique blend of science fiction, action, and historical fiction that will entertain and challenge you. In Amber Harbors’ 11 intriguing stories, we experience one isolated man’s survival as he holds out and awaits the terrifying arrival of otherworldly visitors; firsthand battlefield accounts with some strange occurrences in both WW II and the Revolutionary War; and a tiger hunt in India that goes very wrong. We also see tales of modern woe revolving around some of life’s common miseries, accompanied by brave and unexpected measures to fight against them.</p>
      <p>In addition, we witness an awkward and dangerous stay in an underground bunker with an unstable host; two astronauts stranded on a lifeless asteroid who only have one old-fashioned form of entertainment; an eerie post-plague world dominated by an unlikely species; and an eccentric astronaut orbiting the Earth who is happiest on his own, except for one furry exception. Dale Marbury’s interesting stories travel in different directions, but spring from one deep source: the darker side of the imagination.</p>
    </div>
    <div class="author-photo-slot" role="img" aria-label="Author photo"></div>
    <h3 class="title-caps author-bio-name">DALE MARBURY</h3>
    <div class="author-bio-rule"></div>
    <p class="author-bio">Lorem ipsum dolor sit amet, consectetur adipisicing elit, sed do eiusmod tempor incididunt ut labore et dolore magna aliqua. Ut enim ad minim veniam, quis nostrud exercitation ullamco laboris nisi ut aliquip ex ea commodo consequat. Duis aute irure dolor in reprehenderitt.</p>
  </section>

  <div class="title-caps spine-text">AMBER HARBORS<span class="gap"></span>DALE MARBURY</div>

  <section class="front-cover">
    <p class="title-caps front-author">DALE MARBURY</p>
    <h1 class="title-caps front-title">AMBER<br>HARBORS</h1>
    <p class="title-caps front-subtitle">A COLLECTION OF SHORT STORIES</p>
  </section>
</main>
</body>
</html>
```